Business card design needed

A Moth's Twig

I would like a design for a small business specializing in earrings made from Tasmanian timber combined with coloured beads. I see the brand as a modern take on wooden earrings, fun and beautiful with the wood being laser cut Tasmanian timber combined with a coloured sometimes metallic bead.

I see the logo design as a little cute, perhaps a ladybug on a leaf and would like a combination of green and white. I have seen a quirky take on the traditional red ladybug done in pink with black spots on a green leaf that I like but I'm very open to ideas and suggestions.

Target Market(s)

Women primarily aged 20-50

Industry/Entity Type

Small Business

Contact Information for Business Card

A Moth's Twig
Tasmanian Timber & Beaded Design Earrings

www.friendspage.example/amothstwig
www.craftstall.example.au/amothstwig

Logo Text

A Moth's Twig

Requirements
Must have
• Must have some white on the business card. The cards are being matched with Tasmanian Timber earrings so whites and greens with a splash of colour is okay, but nothing to crazy or bright.

```html
<!DOCTYPE html>
<html lang="en">
<head>
<meta charset="utf-8">
<title>A Moth's Twig – Business Card</title>
<link rel="stylesheet" href="https://fonts.googleapis.com/css2?family=Amatic+SC:wght@400;700&display=swap">
<style>
  :root {
    --paper: #ffffff;
    --bark: #45351c;
    --leaf: #1a8a5a;
    --olive: #6e8b3d;
    --amber: #f7941d;
  }
  html, body {
    margin: 0;
    padding: 0;
    overflow: hidden;
    background: var(--paper);
  }
  .card {
    position: relative;
    width: 1200px;
    height: 693px;
    background: var(--paper);
    overflow: hidden;
    font-family: "Amatic SC", "Arial Narrow", sans-serif;
  }
  .brand {
    position: absolute;
    left: 170px;
    top: 190px;
    width: 415px;
    height: 330px;
    display: flex;
    flex-direction: column;
    align-items: center;
    justify-content: center;
    gap: 26px;
  }
  .brand-dot {
    width: 150px;
    height: 150px;
    border-radius: 50%;
    background: var(--amber);
  }
  .brand-name {
    margin: 0;
    font-weight: 700;
    font-size: 66px;
    line-height: 1;
    color: var(--bark);
    text-transform: lowercase;
    letter-spacing: 1px;
  }
  .details {
    position: absolute;
    left: 640px;
    top: 232px;
    width: 476px;
    text-align: center;
  }
  .tagline {
    margin: 0;
    font-weight: 700;
    font-size: 35px;
    line-height: 46px;
    color: var(--bark);
    letter-spacing: 0.5px;
  }
  .divider {
    display: flex;
    justify-content: center;
    gap: 22px;
    margin: 22px 0 18px;
  }
  .divider span {
    width: 14px;
    height: 14px;
    border-radius: 50%;
    background: var(--olive);
  }
  .links {
    margin: 0;
    padding: 0;
    list-style: none;
    font-weight: 700;
    font-size: 33px;
    line-height: 45px;
    color: var(--leaf);
    letter-spacing: 0.5px;
  }
</style>
</head>
<body>
  <main class="card">
    <div class="brand">
      <div class="brand-dot"></div>
      <p class="brand-name">a moth's twig</p>
    </div>

    <section class="details">
      <p class="tagline">Tasmanian Timber &amp;<br>Beaded Design Earrings</p>
      <div class="divider"><span></span><span></span></div>
      <ul class="links">
        <li>www.friendspage.example/amothstwig</li>
        <li>www.craftstall.example.au/amothstwig</li>
      </ul>
    </section>
  </main>
</body>
</html>
```